Velmoria Blend tea

We are relaunching our new bottle of Guayusa energy tea.
Guayusa is cultivate carefully by The native South American Amazonian farmers, with a diverse mix of food crops, herbs, hardwood trees, fruit trees, spices, medicinal plants and the Guayusa Trees. The farming process that takes place in harmony with the Amazon Rainforest and the diversity of their gardens reflects this attitude toward the natural world.

The company was establish in 2014 and goes by until the pandemic. When all the operations stoped. Now we want to enter again into the USA market with many improvements in the bottle image, we want to use glass bottle so the costumer can look into the color of the tea but with a logo that stand ups, nutritional information and benefits for your health with the Guayusa energy tea
like:
Acecelerate Metabolism
24 Vitamins and Minerals
Burns Calories & Body fat
Provide essential energy

Brewed From Guayusa : used throughout centuries for its healing properties, focused mental clarity, and potent health effects!

Sweetened With Natural Agave :healthy alternative to sugar & artificial sweeteners with a more smooth, flavorful taste than other teas!

Sooth & Stimulating : abundance of caffeine that is slowly released to provide a smooth and pleasant stimulus for waking up in the morning!

Low Glycemic Index :stabilizes blood sugar levels to promote weight loss, boost cardiovascular health & prevent type 2 diabetes!

2 x As Many Antioxidants as Green tea : great for immune system health, eliminating free radicals & fighting/preventing cancer!

Excellent Source of Nutrition — provides an array of 11 polyphenols, 15 amino acids & 24 vitamins and minerals for healthy, balanced diet!

Target Market(s)

eeuu

Industry/Entity Type

beverages industry

Colors
FFC000
F8CF3A
FAE287
FDF2CF
FEFAEE

Requirements
Must have
• Glass bottle designs, full label

```html
<!DOCTYPE html>
<html lang="en">
<head>
<meta charset="utf-8">
<title>Velmoria Blend tea – bottle label</title>
<link rel="stylesheet" href="https://fonts.googleapis.com/css2?family=Montserrat:wght@400;500&display=swap">
<style>
  :root {
    --canvas: #ffffff;
    --label-edge: #e2e2e2;
    --label-mid: #f7f7f7;
    --band: #6b3300;
    --ink: #111111;
    --leaf: #0f6b3a;
    --brand: #3b2210;
  }
  * { box-sizing: border-box; margin: 0; padding: 0; }
  html, body {
    width: 1200px; height: 900px; overflow: hidden;
    background: var(--canvas);
    font-family: "Montserrat", Arial, sans-serif;
    color: var(--ink);
  }
  .label {
    position: absolute;
    left: 378px; top: 30px;
    width: 445px; height: 840px;
    background: linear-gradient(90deg, var(--label-edge) 0%, var(--label-mid) 38%, var(--label-mid) 55%, var(--label-edge) 100%);
  }
  .band {
    position: absolute; left: 0; right: 0; height: 12px;
    background: var(--band);
  }
  .band--top { top: 20px; }
  .band--bottom { top: 808px; }

  .brand-mark {
    position: absolute; left: 0; right: 0; top: 120px;
    display: flex; flex-direction: column; align-items: center; gap: 22px;
  }
  .brand-mark__dot {
    width: 150px; height: 150px; border-radius: 50%;
    background: var(--leaf);
  }
  .brand-mark__name {
    font-size: 30px; font-weight: 500; letter-spacing: 1px;
    color: var(--brand);
  }

  .claims {
    position: absolute; left: 92px; top: 418px;
    width: 260px; height: 108px;
    border: 2px solid var(--ink);
    padding: 8px 12px;
    font-size: 17px; font-weight: 400; line-height: 22.5px; letter-spacing: 0.4px;
  }

  .benefits {
    position: absolute; left: 20px; top: 542px; width: 408px;
    list-style: none;
    font-size: 11.2px; line-height: 13.5px;
  }
  .benefits li {
    position: relative; padding-left: 8px; margin-bottom: 12.5px;
  }
  .benefits li::before {
    content: ""; position: absolute; left: 0; top: 5px;
    width: 4px; height: 4px; border-radius: 50%; background: var(--ink);
  }

  .volume {
    position: absolute; left: 0; right: 0; top: 777px;
    text-align: center; font-size: 20px; font-weight: 500; letter-spacing: 0.5px;
  }
</style>
</head>
<body>
  <section class="label">
    <div class="band band--top"></div>

    <div class="brand-mark">
      <div class="brand-mark__dot"></div>
      <div class="brand-mark__name">Velmoria Blend tea</div>
    </div>

    <div class="claims">
      Acecelerate Metabolism<br>
      24 Vitamins and Minerals<br>
      Burns Calories &amp; Body fat<br>
      Provide essential energy
    </div>

    <ul class="benefits">
      <li>Brewed From Guayusa : used throughout centuries for its healing<br>properties, focused mental clarity, and potent health effects!</li>
      <li>Sweetened With Natural Agave :healthy alternative to sugar &amp; artificial<br>sweeteners with a more smooth, flavorful taste than other teas!</li>
      <li>Sooth &amp; Stimulating : abundance of caffeine that is slowly released to<br>provide a smooth and pleasant stimulus for waking up in the morning!</li>
      <li>Low Glycemic Index :stabilizes blood sugar levels to promote weight<br>loss, boost cardiovascular health &amp; prevent type 2 diabetes!</li>
      <li>2 x As Many Antioxidants as Green tea : great for immune system health,<br>eliminating free radicals &amp; fighting/preventing cancer!</li>
      <li>Excellent Source of Nutrition — provides an array of 11 polyphenols,<br>15 amino acids &amp; 24 vitamins and minerals for healthy, balanced diet!</li>
    </ul>

    <div class="volume">473ML</div>

    <div class="band band--bottom"></div>
  </section>
</body>
</html>
```